Business card design for IT consulting company

Looking for a simple, modern, clean business card design.
Open to reworking our existing logo.

Attached is our current business cards which we do not like.
Ideally double sided with something simple on the back.
Rectangle / Horizonal only.
No rounded edges on the card.
White as the dominate color is preferred.

Target Market(s)

clients, legal, oil & gas, medical, professionals

Industry/Entity Type

IT, tech, consulting

Contact Information for Business Card

Name, Title, email, phone, cell, website

Font styles to use
Sans Serif

Requirements
Must have
• Clean design
Should not have
• loud colors or unusual fonts, etc

```html
<!DOCTYPE html>
<html lang="en">
<head>
<meta charset="utf-8">
<title>Nexa Solutions – Business Card</title>
<link href="https://fonts.googleapis.com/css2?family=Archivo:wght@700&family=Lato:wght@400;700;900&display=swap" rel="stylesheet">
<style>
  :root {
    --backdrop: #141414;
    --paper: #ffffff;
    --ink: #1a1a1a;
    --navy: #27266f;
    --sky: #45b3e2;
    --coral: #ef4056;
    --sun: #f8c630;
    --white: #ffffff;
  }
  * { box-sizing: border-box; margin: 0; padding: 0; }
  html, body {
    width: 1200px; height: 1122px; overflow: hidden;
    background: var(--backdrop);
  }
  .sheet {
    position: relative; width: 1200px; height: 1122px;
    display: flex; flex-direction: column; align-items: center;
    justify-content: center; gap: 42px;
  }
  .card {
    position: relative; width: 875px; height: 500px;
    background: var(--paper); overflow: hidden;
  }
  /* Brand lockup */
  .brand {
    display: flex; align-items: center; gap: 22px;
    font-family: "Archivo", Arial, sans-serif; font-weight: 700;
    color: var(--ink); letter-spacing: -0.5px; white-space: nowrap;
  }
  .brand__square { background: var(--navy); flex: none; }

  /* Front */
  .card--front { display: flex; align-items: center; justify-content: center; }
  .card--front .brand { font-size: 84px; }
  .card--front .brand__square { width: 110px; height: 110px; }

  /* Back */
  .card--back { display: flex; }
  .card__brand-side {
    width: 50%; display: flex; align-items: center; justify-content: center;
    padding: 120px 36px 0 36px;
  }
  .card--back .brand { font-size: 38px; gap: 12px; }
  .card--back .brand__square { width: 56px; height: 56px; }
  .card__info-side {
    width: 50%; background: var(--navy);
    padding: 150px 0 0 70px; font-family: "Lato", Arial, sans-serif;
  }
  .person__name {
    color: var(--sky); font-weight: 900; font-size: 40px;
    text-transform: uppercase; letter-spacing: 0.5px; line-height: 1;
  }
  .person__title {
    color: var(--coral); font-size: 24px; margin-top: 6px; letter-spacing: 0.5px;
  }
  .contact { list-style: none; margin-top: 20px; }
  .contact__item {
    display: flex; align-items: center; gap: 14px;
    color: var(--white); font-size: 22px; letter-spacing: 0.4px;
    line-height: 1; margin-bottom: 14px;
  }
  .contact__icon { width: 22px; height: 22px; flex: none; fill: var(--sun); }
</style>
</head>
<body>
<main class="sheet">
  <section class="card card--front" aria-label="Card front">
    <div class="brand"><span class="brand__square"></span>Nexa Solutions</div>
  </section>

  <section class="card card--back" aria-label="Card back">
    <div class="card__brand-side">
      <div class="brand"><span class="brand__square"></span>Nexa Solutions</div>
    </div>
    <div class="card__info-side">
      <h1 class="person__name">Daniel Reyes</h1>
      <p class="person__title">IT Consultant</p>
      <ul class="contact">
        <li class="contact__item">
          <svg class="contact__icon" viewBox="0 0 24 24"><path d="M6.6 10.8a15.1 15.1 0 0 0 6.6 6.6l2.2-2.2c.3-.3.7-.4 1-.2 1.1.4 2.3.6 3.6.6.6 0 1 .4 1 1V20c0 .6-.4 1-1 1A17 17 0 0 1 3 4c0-.6.4-1 1-1h3.5c.6 0 1 .4 1 1 0 1.3.2 2.5.6 3.6.1.3 0 .7-.2 1z"/></svg>
          (555) 014-2200
        </li>
        <li class="contact__item">
          <svg class="contact__icon" viewBox="0 0 24 24"><path d="M7 1h10a2 2 0 0 1 2 2v18a2 2 0 0 1-2 2H7a2 2 0 0 1-2-2V3a2 2 0 0 1 2-2zm0 3v14h10V4zm5 15.5a1.2 1.2 0 1 0 0 2.4 1.2 1.2 0 0 0 0-2.4z"/></svg>
          (555) 014-3311
        </li>
        <li class="contact__item">
          <svg class="contact__icon" viewBox="0 0 24 24"><path d="M2 5h20v14H2zm2 2v.4l8 5.2 8-5.2V7zm0 2.8V17h16V9.8l-8 5.2z"/></svg>
          daniel.reyes@nexait.ca
        </li>
        <li class="contact__item">
          <svg class="contact__icon" viewBox="0 0 24 24"><path d="M12 2a10 10 0 1 0 0 20 10 10 0 0 0 0-20zm-1 17.9A8 8 0 0 1 4.2 10L9 15v1a2 2 0 0 0 2 2zm6.9-2.5A2 2 0 0 0 16 16h-1v-3a1 1 0 0 0-1-1H8v-2h2a1 1 0 0 0 1-1V7h2a2 2 0 0 0 2-2v-.4a8 8 0 0 1 2.9 12.8z"/></svg>
          www.nexait.ca
        </li>
      </ul>
    </div>
  </section>
</main>
</body>
</html>
```